Medical Company in need of Modern business card design for new Wound Care clinic.

Modern business card design for our Woundcare company. Logo and description of services can be found on our website; https://www.tovrel-woundcare.com/

```html
<!DOCTYPE html>
<html lang="en">
<head>
<meta charset="utf-8">
<title>Tovrel Wound Clinic – Business Card</title>
<link rel="stylesheet" href="https://fonts.googleapis.com/css2?family=Arimo:wght@400;700&display=swap">
<style>
  :root {
    --page: #e6e6e4;
    --paper: #f4f4f2;
    --charcoal: #2f2f30;
    --charcoal-deep: #1c1c1d;
    --gold: #c08a2c;
    --gold-edge: #b88426;
    --ink: #5a5a5a;
    --rule: #6d6d6d;
  }
  * { box-sizing: border-box; margin: 0; padding: 0; }
  html, body { width: 1200px; height: 801px; overflow: hidden; }
  body {
    background: var(--page);
    font-family: "Arimo", Arial, sans-serif;
    position: relative;
  }
  .card {
    position: absolute;
    top: 246px;
    width: 540px;
    height: 309px;
    border: 3px solid var(--gold-edge);
    overflow: hidden;
  }
  .card--front { left: 40px; background: var(--paper); }
  .card--back { left: 620px; background: var(--charcoal); }

  .brand-name {
    font-family: "Arimo", Arial, sans-serif;
    font-weight: 400;
    color: var(--gold);
    letter-spacing: 0.02em;
    white-space: nowrap;
  }
  .card--front .brand-name {
    position: absolute;
    top: 60px;
    left: 0;
    right: 0;
    text-align: center;
    font-size: 28px;
  }
  .card--back .brand-name {
    position: absolute;
    top: 32px;
    right: 36px;
    font-size: 28px;
  }

  .holder {
    position: absolute;
    left: 40px;
    top: 128px;
  }
  .holder__name {
    font-weight: 700;
    font-size: 20px;
    color: var(--gold);
    letter-spacing: 0.01em;
    text-transform: uppercase;
  }
  .holder__role {
    font-size: 15px;
    color: var(--ink);
    margin-top: 1px;
  }
  .divider {
    position: absolute;
    left: 40px;
    right: 40px;
    top: 180px;
    height: 1px;
    background: var(--rule);
  }
  .contacts {
    position: absolute;
    left: 40px;
    top: 196px;
    list-style: none;
  }
  .contacts li {
    display: flex;
    align-items: center;
    gap: 10px;
    font-size: 14.5px;
    color: var(--ink);
    line-height: 24px;
  }
  .contacts svg { width: 14px; height: 14px; flex: none; }
  .address {
    position: absolute;
    right: 40px;
    top: 196px;
    text-align: right;
    font-style: normal;
    font-size: 14.5px;
    line-height: 24px;
    color: var(--ink);
  }

  .back-decoration {
    position: absolute;
    left: 0;
    bottom: 0;
    width: 100%;
    height: 100%;
  }
</style>
</head>
<body>
  <section class="card card--front" aria-label="Business card front">
    <h1 class="brand-name">Tovrel Wound Clinic</h1>

    <div class="holder">
      <p class="holder__name">Marcus Hale</p>
      <p class="holder__role">Manager</p>
    </div>

    <div class="divider"></div>

    <ul class="contacts">
      <li>
        <svg viewBox="0 0 16 16" aria-hidden="true"><path d="M3 1.5l3 3-1.6 1.6a9 9 0 0 0 5.5 5.5L11.5 10l3 3-2 2C6.5 15 1 9.5 1 3.5z" fill="none" stroke="#c08a2c" stroke-width="1.4" stroke-linejoin="round"/></svg>
        555-014-2290
      </li>
      <li>
        <svg viewBox="0 0 16 16" aria-hidden="true"><rect x="1" y="3" width="14" height="10" fill="none" stroke="#c08a2c" stroke-width="1.4"/><path d="M1 3l7 6 7-6" fill="none" stroke="#c08a2c" stroke-width="1.4"/></svg>
        info@tovrel-woundcare.com
      </li>
      <li>
        <svg viewBox="0 0 16 16" aria-hidden="true"><circle cx="8" cy="8" r="6.5" fill="none" stroke="#c08a2c" stroke-width="1.3"/><ellipse cx="8" cy="8" rx="3" ry="6.5" fill="none" stroke="#c08a2c" stroke-width="1.1"/><path d="M1.5 8h13M2.5 4.8h11M2.5 11.2h11" stroke="#c08a2c" stroke-width="1.1"/></svg>
        www.tovrel-woundcare.com
      </li>
    </ul>

    <address class="address">
      1820 Linden Ave Ste 200<br>
      PMB 208316 Avonford, TX 75040
    </address>
  </section>

  <section class="card card--back" aria-label="Business card back">
    <svg class="back-decoration" viewBox="0 0 534 303" preserveAspectRatio="none" role="img" aria-label="Large embossed brand symbol decoration in dark grey tones">
      <defs>
        <linearGradient id="emboss" x1="0" y1="1" x2="1" y2="0">
          <stop offset="0" stop-color="#1c1c1d"/>
          <stop offset="0.6" stop-color="#3a3a3c"/>
          <stop offset="1" stop-color="#2f2f30"/>
        </linearGradient>
      </defs>
      <path d="M0 110 L330 303 L0 303 Z" fill="url(#emboss)"/>
    </svg>
    <p class="brand-name">Tovrel Wound Clinic</p>
  </section>
</body>
</html>
```